Postcard for dumpster rental business

We need an attractive post card to entice other businesses to use our dumpster rental service. This is a business to business situation.
Target Market(s)
Roofing, property restoration and remodeling contractors
Industry/Entity Type
Dumpster rentals
Font styles to use
Sans Serif
Colors
0054AA
0677BA
7BADD7
CADEEF
E8F1F8
Requirements
Must have
- tossbinhaul.com Dumpster rental Easy online booking Logo Guaranteed On Time Delivery (as a badge or button?) QR Code Picture of our dumpster (see website)
Nice to have
- Call to action "Order now!"

```html
<!DOCTYPE html>
<html lang="en">
<head>
<meta charset="utf-8">
<title>Tossbin Haul Dumpster Rental – Postcard</title>
<link rel="stylesheet" href="https://fonts.googleapis.com/css2?family=Lato:wght@400;700;900&family=Oswald:wght@400;500;600&display=swap">
<style>
  :root {
    --backdrop: #8a8a8a;
    --blue-deep: #0054aa;
    --blue-mid: #0677ba;
    --blue-bright: #1f7fd6;
    --navy: #2c2a86;
    --orange: #e8661c;
    --orange-light: #f07a25;
    --yellow: #ffe21a;
    --white: #ffffff;
    --panel: #ececec;
    --ink: #333333;
    --ink-soft: #444444;
  }
  * { box-sizing: border-box; margin: 0; padding: 0; }
  html, body { width: 900px; height: 1200px; overflow: hidden; }
  body { background: var(--backdrop); font-family: "Lato", sans-serif; position: relative; }

  .card { position: absolute; overflow: hidden; box-shadow: 0 6px 18px rgba(0,0,0,.35); }
  .card svg.shapes { position: absolute; inset: 0; }

  /* ---------- Front ---------- */
  .card-front { left: 40px; top: 63px; width: 688px; height: 492px; background: var(--blue-bright); }
  .front-logo {
    position: absolute; left: 28px; top: 70px; width: 182px; height: 107px;
    background: var(--white); border-radius: 50%;
    display: flex; flex-direction: column; align-items: center; justify-content: center;
    color: var(--blue-deep); font-weight: 900; text-align: center; line-height: 1.05;
  }
  .front-logo .brand { font-size: 22px; letter-spacing: .5px; }
  .front-logo .sub { font-size: 11px; letter-spacing: 1px; }
  .front-logo .phone { font-size: 9px; letter-spacing: .5px; }
  .front-photo {
    position: absolute; left: 345px; top: 14px; width: 330px; height: 236px;
    border-radius: 4px;
    background: linear-gradient(160deg, #f5a23a 0%, #ec7e1f 45%, #cf5f14 100%);
  }
  .headline-small {
    position: absolute; left: 24px; top: 334px; color: var(--white);
    font-size: 26px; font-weight: 400; letter-spacing: .3px;
  }
  .headline-large {
    position: absolute; left: 22px; top: 363px; color: var(--navy);
    font-size: 42px; font-weight: 900; letter-spacing: -.3px;
  }
  .order-button {
    position: absolute; left: 482px; top: 339px; width: 168px; height: 68px;
    border: 4px solid var(--white); border-radius: 34px;
    display: flex; align-items: center; justify-content: center;
  }
  .order-button span {
    background: var(--orange); color: var(--white); border: 3px solid var(--white); border-radius: 24px;
    font-family: "Oswald", sans-serif; font-weight: 500; font-size: 24px; padding: 2px 12px 4px;
  }
  .order-button svg { position: absolute; right: 8px; bottom: -12px; }
  .feature-strip { position: absolute; left: 0; top: 427px; width: 688px; height: 38px; }
  .feature-booking {
    position: absolute; left: 18px; top: 0; height: 38px; line-height: 38px;
    color: var(--ink); font-size: 19px; font-weight: 700; letter-spacing: .9px;
  }
  .feature-delivery {
    position: absolute; left: 312px; top: 0; height: 38px; line-height: 38px;
    color: var(--white); font-size: 20px; font-weight: 400;
  }
  .feature-delivery strong { color: var(--yellow); font-weight: 900; }

  /* ---------- Back ---------- */
  .card-back { left: 190px; top: 618px; width: 656px; height: 470px; background: var(--white); }
  .about-tag {
    position: absolute; left: 0; top: 29px; height: 22px; width: 112px;
    background: var(--orange); color: var(--white); font-size: 14px; font-weight: 700;
    line-height: 22px; padding-left: 25px;
    clip-path: polygon(0 0, 94% 0, 100% 50%, 94% 100%, 0 100%);
  }
  .about-text {
    position: absolute; left: 22px; top: 65px; width: 196px;
    font-size: 10px; line-height: 12.5px; color: var(--ink);
  }
  .take-title { position: absolute; left: 22px; top: 190px; line-height: 1; }
  .take-title .small { display: block; font-size: 16px; font-weight: 900; color: var(--ink); }
  .take-title .big { display: block; font-size: 27px; font-weight: 900; color: var(--orange); margin-top: 2px; }
  .service-list { position: absolute; top: 248px; list-style: none; font-size: 10.5px; color: var(--ink); width: 140px; }
  .service-list li { position: relative; padding-left: 14px; line-height: 13px; margin-bottom: 4px; }
  .service-list li::before {
    content: ""; position: absolute; left: 1px; top: 4px; width: 5px; height: 5px;
    border-radius: 50%; background: var(--orange);
  }
  .service-list.col-1 { left: 22px; }
  .service-list.col-2 { left: 178px; width: 120px; }
  .back-logo {
    position: absolute; left: 22px; top: 398px; width: 100px; text-align: center;
    color: var(--blue-deep); font-weight: 900; line-height: 1.05;
  }
  .back-logo .brand { font-size: 13px; }
  .back-logo .sub { font-size: 7px; letter-spacing: .6px; }
  .call-bar {
    position: absolute; left: 140px; top: 380px; width: 320px; height: 52px;
    background: var(--navy); color: var(--white);
    clip-path: polygon(7% 0, 100% 0, 100% 100%, 7% 100%, 0 50%);
    display: flex; align-items: center; font-family: "Oswald", sans-serif;
  }
  .call-bar .label { margin-left: 42px; font-size: 20px; font-weight: 500; padding-right: 14px; border-right: 1px solid rgba(255,255,255,.7); line-height: 30px; }
  .call-bar .phone { margin-left: 22px; font-size: 20px; color: var(--orange-light); }
  .back-dumpster {
    position: absolute; left: 455px; top: 366px; width: 201px; height: 80px;
    background: linear-gradient(180deg, #f7891f 0%, #e8691a 60%, #c8520f 100%);
    clip-path: polygon(0 0, 100% 0, 100% 100%, 6% 100%, 3% 20%);
  }
  .stamp-box { position: absolute; left: 575px; top: 31px; width: 57px; height: 63px; border: 1px solid var(--ink-soft); background: var(--white); }
  .address-line { position: absolute; left: 437px; width: 190px; height: 1px; background: var(--ink-soft); }
  .address-line.line-1 { top: 168px; }
  .address-line.line-2 { top: 201px; }
  .address-line.line-3 { top: 234px; }
</style>
</head>
<body>

<section class="card card-front" aria-label="Postcard front">
  <svg class="shapes" width="688" height="492" viewBox="0 0 688 492">
    <defs>
      <linearGradient id="sky" x1="0" y1="0" x2="0" y2="1">
        <stop offset="0" stop-color="#2a8ae0"/>
        <stop offset="1" stop-color="#0b55b0"/>
      </linearGradient>
      <linearGradient id="flame" x1="0" y1="0" x2="1" y2="0">
        <stop offset="0" stop-color="#f0561e"/>
        <stop offset="1" stop-color="#d52a1c"/>
      </linearGradient>
    </defs>
    <rect width="688" height="492" fill="url(#sky)"/>
    <path class="swoosh-navy" d="M0,0 L100,0 C55,70 95,190 320,250 C470,285 610,270 688,240 L688,320 C560,335 380,330 240,300 C100,270 0,210 0,170 Z" fill="var(--navy)"/>
    <path class="swoosh-red" d="M0,150 C70,250 260,320 688,316 L688,330 C300,345 80,300 0,215 Z" fill="url(#flame)"/>
    <path class="panel-orange" d="M0,200 C100,290 300,335 688,330 L688,492 L0,492 Z" fill="var(--orange)"/>
    <polygon points="0,427 280,427 295,446 280,465 0,465" fill="#eeeeee"/>
    <polygon points="286,427 688,427 688,465 286,465 301,446" fill="#1f6fd2"/>
    <rect x="0" y="465" width="688" height="27" fill="var(--orange)"/>
  </svg>

  <div class="front-photo" role="img" aria-label="Photo of a worker tossing debris into an orange roll-off dumpster"></div>

  <div class="front-logo">
    <span class="brand">TOSSBIN</span>
    <span class="sub">DUMPSTER RENTAL</span>
    <span class="phone">(555) 204-7716</span>
  </div>

  <h1 class="headline-small">DUMPSTER RENTAL AND</h1>
  <h2 class="headline-large">REMOVAL SERVICES</h2>

  <div class="order-button">
    <span>ORDER NOW!!</span>
    <svg width="30" height="32" viewBox="0 0 30 32" aria-hidden="true">
      <path d="M3,2 L3,26 L9,20 L14,30 L19,28 L14,18 L22,18 Z" fill="var(--white)" stroke="var(--orange)" stroke-width="1.5"/>
    </svg>
  </div>

  <div class="feature-strip">
    <p class="feature-booking">EASY ONLINE BOOKING</p>
    <p class="feature-delivery"><strong>GUARANTEED</strong> ON TIME DELIVERY</p>
  </div>
</section>

<section class="card card-back" aria-label="Postcard back">
  <svg class="shapes" width="656" height="470" viewBox="0 0 656 470">
    <rect width="656" height="470" fill="var(--panel)"/>
    <path class="swoosh-orange" d="M205,0 L222,0 C262,150 340,300 656,362 L656,372 C320,320 240,180 205,0 Z" fill="var(--orange)"/>
    <path class="swoosh-navy" d="M218,0 L656,0 L656,362 C360,300 262,150 218,0 Z" fill="var(--navy)"/>
    <path class="address-area" d="M290,0 L656,0 L656,350 C420,320 320,180 290,0 Z" fill="var(--white)"/>
  </svg>

  <div class="about-tag">ABOUT US</div>
  <p class="about-text">Tossbin Haul Dumpster Rental is locally owned and operated by a small-business team with a reputation that spans over 30 years. Our competitive prices and high standards allow us to offer comprehensive, professional, and personalized customer-service to meet your practical and financial needs.</p>

  <h3 class="take-title"><span class="small">WE TAKE JUST ABOUT</span><span class="big">EVERYTHING</span></h3>
  <ul class="service-list col-1">
    <li>Refrigerator Disposal</li>
    <li>Garbage Removal</li>
    <li>Mattress Disposal</li>
    <li>Foreclosure Clean Outs</li>
    <li>Construction Waste Removal</li>
    <li>Yard Waste Removal</li>
  </ul>
  <ul class="service-list col-2">
    <li>Trash Removal</li>
    <li>Appliance Removal</li>
    <li>Television Disposal &amp; Recycling</li>
    <li>Furniture Removal</li>
    <li>E-Waste Disposal</li>
    <li>Hot Tub Disposal</li>
  </ul>

  <div class="back-logo">
    <div class="brand">TOSSBIN</div>
    <div class="sub">DUMPSTER RENTAL</div>
    <div class="sub">(555) 204-7716</div>
  </div>

  <div class="back-dumpster" role="img" aria-label="Photo of an orange roll-off dumpster"></div>

  <div class="call-bar">
    <span class="label">GIVE US A CALL</span>
    <span class="phone">(555) 204-7716</span>
  </div>

  <div class="stamp-box" aria-label="Stamp area"></div>
  <div class="address-line line-1"></div>
  <div class="address-line line-2"></div>
  <div class="address-line line-3"></div>
</section>

</body>
</html>
```